3 Business Card designs for a company with multiple services

We are a company that has 3 main services:

1) Security - CCTV & Alarm Sepcialists
2) Broadcast - Broadcast Sales and Technical Services
3) Distribution - Quality Products, Quality Service

The broadcast service is for Video Broadcast.

I will include our logos for each service.

I would like to also create a business card design for 5QM in general (see main logo).

Each card will be two-sided. On the front I would think it would include Logo, Name, Posistion and Mobile (and possibly email). And possibly our main number (which may be something like 1800 639 415)

On the back it MUST include a "lined" section to be able to write short quotes / prices.

Then include more details like Phone: 1800 639 415 Fax: 1800 639 417 Postal: PO Box 317, Tallowbrook, QLD Australia 4219 Website: www.5qm.com.au

We would like a fresh, inovative card design with that "wow check this out" feel about it.

Look forward to seeing what you can do! :)

Corin

Industry/Entity Type

Business

Requirements
Must have
• Quote section on the back!
Editable files.

```html
<!DOCTYPE html>
<html lang="en">
<head>
<meta charset="utf-8">
<title>5QM Business Cards</title>
<link rel="stylesheet" href="https://fonts.googleapis.com/css2?family=Roboto+Slab:wght@400;700&family=Roboto+Condensed:wght@400;700&display=swap">
<style>
  :root {
    --page: #ffffff;
    --card-grey: #c9c9c9;
    --ink: #1e1e1e;
    --ink-soft: #3a3a3a;
    --rule: #555555;
    --border: #9a9a9a;
    --tile: #1a1a1a;
    --security: #e0402a;
    --broadcast: #e9ae22;
    --distribution: #2370b8;
    --group: #2b2b2b;
    --white: #ffffff;
  }
  * { box-sizing: border-box; margin: 0; padding: 0; }
  html, body { width: 1057px; height: 1200px; overflow: hidden; background: var(--page); }
  body { position: relative; font-family: "Roboto Slab", Georgia, serif; color: var(--ink); }

  .card { position: absolute; width: 454px; height: 271px; overflow: hidden; }
  .col-a { left: 46px; } .col-b { left: 552px; }
  .row-1f { top: 33px; } .row-1b { top: 314px; }
  .row-2f { top: 608px; } .row-2b { top: 888px; }

  .security { --accent: var(--security); }
  .broadcast { --accent: var(--broadcast); }
  .distribution { --accent: var(--distribution); }
  .group { --accent: var(--group); }

  /* Front */
  .front { background: var(--card-grey); }
  .brand { position: absolute; left: 0; top: 0; height: 88px; display: flex; }
  .brand-mark { width: 84px; height: 88px; background: var(--accent); }
  .brand-name {
    margin-left: 4px; width: 186px; height: 88px; background: var(--tile); color: var(--white);
    font-weight: 700; display: flex; flex-direction: column; justify-content: center; align-items: center;
  }
  .brand-name .word { font-size: 40px; letter-spacing: 14px; line-height: 1; padding-left: 14px; }
  .brand-name .service { font-size: 15px; letter-spacing: 5px; margin-top: 6px; padding-left: 5px; }

  .person { position: absolute; left: 26px; top: 120px; }
  .person-name { font-size: 19px; line-height: 24px; }
  .person-role { font-size: 17px; line-height: 22px; color: var(--ink-soft); }
  .contacts { position: absolute; left: 26px; top: 172px; list-style: none; font-size: 14.5px; line-height: 19.7px; }
  .contacts li { display: flex; align-items: center; gap: 5px; }
  .key {
    display: inline-flex; width: 14px; height: 14px; background: var(--accent); color: var(--white);
    font-size: 10px; font-weight: 700; align-items: center; justify-content: center;
    font-family: "Roboto Condensed", Arial, sans-serif;
  }
  .tagline {
    position: absolute; right: 18px; bottom: 12px; font-family: "Roboto Condensed", Arial, sans-serif;
    font-size: 10.5px; color: var(--accent);
  }

  /* Back */
  .back { background: var(--white); border: 1px solid var(--border); border-top-right-radius: 58px; }
  .quote-lines { position: absolute; left: 22px; right: 22px; top: 48px; }
  .quote-lines span { display: block; height: 29px; border-top: 1.5px solid var(--rule); }
  .details {
    position: absolute; left: 0; right: 0; bottom: 0; height: 130px; background: var(--accent);
    color: var(--white); text-align: center; font-size: 13px; line-height: 20.5px; padding-top: 58px;
  }
  .group .details { background: transparent; color: var(--ink); padding-top: 48px; }
  .group .quote-lines { top: 58px; }

  /* Group front */
  .group-front { background: #f0f0f0; }
  .group-head { position: absolute; left: 0; top: 0; width: 100%; height: 106px; background: linear-gradient(#4a4a4a, #1c1c1c); }
  .group-head .brand-name { position: absolute; right: 0; top: 0; height: 73px; width: 225px; margin: 0; background: var(--tile); }
  .group-head .brand-name .word { font-size: 44px; }
  .group-mark { position: absolute; left: 22px; top: 16px; width: 40px; height: 40px; background: #8a8a8a; }
  .group-strip {
    position: absolute; left: 0; bottom: 0; width: 100%; height: 33px; background: #000; color: var(--white);
    font-family: "Roboto Condensed", Arial, sans-serif; font-weight: 700; font-size: 19px; letter-spacing: 1.5px;
    display: flex; align-items: center; padding-left: 14px;
  }
  .field { position: absolute; left: 26px; right: 18px; display: flex; align-items: flex-end; gap: 6px; font-size: 13px; }
  .field .blank { flex: 1; border-bottom: 1.5px solid var(--rule); margin-bottom: 3px; }
  .field-name { top: 150px; }
  .field-role { top: 186px; font-size: 12px; }
  .group-contacts { position: absolute; left: 26px; top: 233px; display: flex; gap: 12px; font-size: 14px; align-items: center; }
  .group-contacts span { display: flex; align-items: center; gap: 5px; }
  .group-contacts .key { background: var(--tile); }
</style>
</head>
<body>

<!-- Security -->
<section class="card front security col-a row-1f">
  <div class="brand"><div class="brand-mark"></div><div class="brand-name"><span class="word">5QM</span><span class="service">SECURITY</span></div></div>
  <div class="person"><p class="person-name">Dylan Marsh</p><p class="person-role">Manager</p></div>
  <ul class="contacts">
    <li><span class="key">M</span>91 4826 305</li>
    <li><span class="key">T</span>1800 639 415</li>
    <li><span class="key">E</span>dylan@5qm.com.au</li>
    <li><span class="key">W</span>www.5qm.com.au</li>
  </ul>
  <p class="tagline">CCTV &amp; Alarm Specialists</p>
</section>
<section class="card back security col-a row-1b">
  <div class="quote-lines"><span></span><span></span><span></span></div>
  <div class="details">
    <p>Phone: 1800 639 415 | Fax: 1800 639 417</p>
    <p>Postal: PO Box 317, Tallowbrook, QLD Australia 4219</p>
    <p>Website: www.5qm.com.au</p>
  </div>
</section>

<!-- Broadcast -->
<section class="card front broadcast col-b row-1f">
  <div class="brand"><div class="brand-mark"></div><div class="brand-name"><span class="word">5QM</span><span class="service">BROADCAST</span></div></div>
  <div class="person"><p class="person-name">Dylan Marsh</p><p class="person-role">Manager</p></div>
  <ul class="contacts">
    <li><span class="key">M</span>91 4826 305</li>
    <li><span class="key">T</span>1800 639 415</li>
    <li><span class="key">E</span>dylan@5qm.com.au</li>
    <li><span class="key">W</span>www.5qm.com.au</li>
  </ul>
  <p class="tagline">Broadcast Sales and Technical Services</p>
</section>
<section class="card back broadcast col-b row-1b">
  <div class="quote-lines"><span></span><span></span><span></span></div>
  <div class="details">
    <p>Phone: 1800 639 415 | Fax: 1800 639 417</p>
    <p>Postal: PO Box 317, Tallowbrook, QLD Australia 4219</p>
    <p>Website: www.5qm.com.au</p>
  </div>
</section>

<!-- Distribution -->
<section class="card front distribution col-a row-2f">
  <div class="brand"><div class="brand-mark"></div><div class="brand-name"><span class="word">5QM</span><span class="service">DISTRIBUTION</span></div></div>
  <div class="person"><p class="person-name">Dylan Marsh</p><p class="person-role">Manager</p></div>
  <ul class="contacts">
    <li><span class="key">M</span>91 4826 305</li>
    <li><span class="key">T</span>1800 639 415</li>
    <li><span class="key">E</span>dylan@5qm.com.au</li>
    <li><span class="key">W</span>www.5qm.com.au</li>
  </ul>
  <p class="tagline">Quality Products, Quality Service</p>
</section>
<section class="card back distribution col-a row-2b">
  <div class="quote-lines"><span></span><span></span><span></span></div>
  <div class="details">
    <p>Phone: 1800 639 415 | Fax: 1800 639 417</p>
    <p>Postal: PO Box 317, Tallowbrook, QLD Australia 4219</p>
    <p>Website: www.5qm.com.au</p>
  </div>
</section>

<!-- Group -->
<section class="card group-front group col-b row-2f">
  <div class="group-head">
    <div class="group-mark"></div>
    <div class="brand-name"><span class="word">5QM</span></div>
    <div class="group-strip">SECURITY - BROADCAST - DISTRIBUTION</div>
  </div>
  <div class="field field-name"><span>Name :</span><span class="blank"></span></div>
  <div class="field field-role"><span>Designation :</span><span class="blank"></span></div>
  <div class="group-contacts">
    <span><span class="key">T</span>1800 639 415</span>
    <span><span class="key">E</span>user@5qm.com.au</span>
    <span><span class="key">W</span>www.5qm.com.au</span>
  </div>
</section>
<section class="card back group col-b row-2b">
  <div class="quote-lines"><span></span><span></span><span></span><span></span></div>
  <div class="details">
    <p>Phone: 1800 639 415 | Fax: 1800 639 417</p>
    <p>Postal: PO Box 317, Tallowbrook, QLD Australia 4219</p>
    <p>Website: www.5qm.com.au</p>
  </div>
</section>

</body>
</html>
```